I need a wordpress website for myconsulting company specialized in data privacy

I'm looking for a wordpress website for my consulting company specialized in data privacy (GDPR) and computer science.
The website will serve as entry point to for potential clients.
The website should have the following sections (I'm opened to new ideas):
- Presentation of the company
- General presentation
- Services provided with some details
- Blog/articles with tags (if possible)
- Contact
On every page of the website there should be some references to pages (such as privacy policy, legal information...)
If possible he website should be multinlingual (english and french). I'll personnally take care of the translation in french.
Regarding branding;
- Name of the company: Laurent Dubreuil Conseil
- Logo is attached
- For colors to be used see attached PDF for exemple

```html
<!DOCTYPE html>
<html lang="en">
<head>
<meta charset="utf-8">
<title>Laurent Dubreuil Conseil — Data Privacy Consulting</title>
<link href="https://fonts.googleapis.com/css2?family=Righteous&family=Poppins:wght@400;500;600&display=swap" rel="stylesheet">
<style>
:root{
  --ink:#0d1b2a;
  --text:#4a5563;
  --teal:#0c7a8c;
  --teal-deep:#0b6f86;
  --green:#24ad8e;
  --navy:#0a2c4b;
  --navy-deep:#082440;
  --lavender:#f3f3fb;
  --white:#ffffff;
  --line:#e6e8ee;
}
*{margin:0;padding:0;box-sizing:border-box}
html,body{width:1200px;height:3808px;overflow:hidden;background:var(--white)}
body{position:relative;font-family:"Poppins",sans-serif;color:var(--text)}
.abs{position:absolute}
.display{font-family:"Righteous",sans-serif;color:var(--ink);font-weight:400}
.btn{position:absolute;display:flex;align-items:center;justify-content:center;font-size:13px;font-weight:600;text-transform:uppercase;letter-spacing:.3px;border-radius:3px}
.btn--solid{background:var(--teal);color:var(--white)}
.btn--outline{border:2px solid var(--ink);color:var(--ink);background:var(--white)}
.placeholder{position:absolute}

/* header */
.brand{position:absolute;display:flex;align-items:center;gap:10px}
.brand__mark{width:28px;height:28px;background:var(--teal)}
.brand__name{font-family:"Poppins",sans-serif;font-weight:500;color:var(--teal-deep);font-size:18px;white-space:nowrap}
.nav{position:absolute;top:26px;left:550px;display:flex;gap:0;font-size:13px;font-weight:500;color:var(--ink)}
.nav a{position:absolute;white-space:nowrap;text-decoration:none;color:var(--ink)}
.nav a.active{color:var(--teal)}

/* hero */
.hero__title{left:87px;top:284px;font-size:46px;line-height:46px;letter-spacing:.5px}

/* about */
.eyebrow{font-family:"Righteous",sans-serif;color:var(--teal);font-size:26px}
.about__title{left:590px;top:814px;font-size:46px;line-height:46px}
.about__text{left:591px;top:922px;width:520px;font-size:15px;line-height:24.6px}

/* services */
.services__title{left:0;width:1200px;top:1448px;text-align:center;font-size:46px;color:var(--white)}
.services__sub{left:0;width:1200px;top:1502px;text-align:center;font-size:15px;color:var(--white)}
.service-card{position:absolute;top:1552px;width:248px;height:287px;background:var(--white);border-radius:2px;padding:0 22px}
.service-card svg{position:absolute;left:22px;top:36px}
.service-card h3{position:absolute;left:22px;top:125px;font-family:"Righteous",sans-serif;font-weight:400;color:var(--ink);font-size:18px;white-space:nowrap}
.service-card p{position:absolute;left:22px;top:154px;width:210px;font-size:13px;line-height:20px}
.link{font-size:14px;font-weight:600;color:var(--teal);text-transform:uppercase;letter-spacing:.3px}
.service-card .link{position:absolute;left:22px;top:234px}

/* projects */
.projects__title{left:86px;top:2142px;font-size:46px;line-height:46px}
.projects__text{left:86px;top:2254px;width:450px;font-size:15px;line-height:24.6px}
.project-tile{position:absolute;top:2096px;width:248px;height:287px;overflow:hidden}
.project-tile span{position:absolute;left:42px;bottom:30px;font-family:"Righteous",sans-serif;color:var(--white);font-size:21px;line-height:21px}

/* blog */
.blog__title{left:0;width:1200px;top:2508px;text-align:center;font-size:46px}
.blog__sub{left:0;width:1200px;top:2562px;text-align:center;font-size:15px}
.post{position:absolute;top:2612px;width:331px;height:422px;background:var(--white);box-shadow:0 4px 18px rgba(13,27,42,.09)}
.post__image{position:absolute;left:0;top:0;width:331px;height:236px}
.post h3{position:absolute;left:32px;top:270px;font-family:"Righteous",sans-serif;font-weight:400;color:var(--ink);font-size:22px}
.post p{position:absolute;left:32px;top:306px;width:280px;font-size:13.5px;line-height:20.5px}
.post .link{position:absolute;left:32px;top:376px;font-size:13.5px}

/* newsletter */
.newsletter{position:absolute;left:89px;top:3141px;width:1022px;height:193px;border-radius:30px;background:linear-gradient(90deg,var(--teal-deep),var(--green))}
.newsletter h2{position:absolute;left:65px;top:58px;font-family:"Righteous",sans-serif;font-weight:400;color:var(--white);font-size:46px}
.newsletter p{position:absolute;left:66px;top:118px;color:var(--white);font-size:15px}
.newsletter__field{position:absolute;left:456px;top:71px;width:336px;height:51px;background:var(--white);display:flex;align-items:center;padding-left:26px;font-size:16px;color:#6b7380}
.newsletter__submit{position:absolute;left:792px;top:71px;width:175px;height:51px;background:var(--navy);color:var(--white);display:flex;align-items:center;justify-content:center;font-weight:600;font-size:17px}

/* footer */
.footer-col h4{font-family:"Righteous",sans-serif;font-weight:400;color:var(--green);font-size:24px;margin-bottom:14px}
.footer-col{position:absolute;top:3480px}
.footer-col li{list-style:none;color:#dfe7ef;font-size:12.5px;line-height:22px}
.contact-line{display:flex;align-items:center;gap:9px}
.contact-line svg{flex:none}
.socials{display:flex;gap:16px;margin-top:10px}
.socials i{display:block;width:11px;height:11px;border-radius:50%;background:#dfe7ef}
.copyright{left:87px;top:3768px;color:var(--white);font-size:15px}
.legal{top:3768px;color:var(--white);font-size:15px}
.to-top{left:1130px;top:3727px;width:40px;height:40px;border-radius:50%;background:var(--teal);display:flex;align-items:center;justify-content:center}
</style>
</head>
<body>

<!-- background shapes -->
<svg class="abs" style="left:0;top:0" width="1200" height="3808" aria-hidden="true">
  <defs>
    <linearGradient id="teal-band" x1="0" y1="0" x2="1" y2="1">
      <stop offset="0" stop-color="#0b7d8d"/>
      <stop offset="1" stop-color="#1fa58c"/>
    </linearGradient>
    <linearGradient id="hero-haze" x1="0" y1="0" x2="0" y2="1">
      <stop offset="0" stop-color="#ffffff"/>
      <stop offset="1" stop-color="#f1f1fa"/>
    </linearGradient>
  </defs>
  <path d="M0 540 C180 470 320 600 520 560 C760 510 900 250 1200 160 L1200 660 C900 700 600 640 0 700 Z" fill="url(#hero-haze)"/>
  <path d="M0 1270 C120 1330 260 1360 420 1320 C600 1270 640 1180 860 1190 C1020 1196 1120 1200 1200 1230 L1200 1966 L0 1966 Z" fill="url(#teal-band)"/>
  <path d="M0 3300 C250 3230 500 3280 760 3250 C950 3228 1100 3240 1200 3260 L1200 3808 L0 3808 Z" fill="var(--navy)"/>
</svg>

<!-- header -->
<header>
  <div class="brand" style="left:88px;top:24px">
    <span class="brand__mark"></span>
    <span class="brand__name">Laurent Dubreuil Conseil</span>
  </div>
  <nav class="nav">
    <a class="active" style="left:0">HOME</a>
    <a style="left:68px">ABOUT</a>
    <a style="left:142px">SERVICES</a>
    <a style="left:233px">BLOG</a>
    <a style="left:297px">CONTACT US</a>
  </nav>
  <svg class="abs" style="left:966px;top:29px" width="15" height="15" viewBox="0 0 15 15" aria-label="Search">
    <circle cx="6" cy="6" r="4.8" fill="none" stroke="#333" stroke-width="1.5"/>
    <line x1="9.6" y1="9.6" x2="13.5" y2="13.5" stroke="#333" stroke-width="1.5"/>
  </svg>
  <div class="btn btn--solid" style="left:993px;top:21px;width:118px;height:30px;font-size:11px">Get a quote</div>
</header>

<!-- hero -->
<section class="hero">
  <h1 class="display abs hero__title">Data privacy<br>Solutions Built On<br>Customer Trust</h1>
  <div class="btn btn--solid" style="left:89px;top:440px;width:136px;height:40px">Get started</div>
  <div class="btn btn--outline" style="left:231px;top:440px;width:136px;height:40px">About us</div>
  <div class="placeholder" role="img" aria-label="Isometric illustration of a monitor with a security shield connected to glowing data nodes"
       style="left:569px;top:163px;width:631px;height:473px;border-radius:50%;background:radial-gradient(ellipse at center,#cfeef0 0%,#e7eaf8 45%,rgba(243,243,251,0) 72%)"></div>
</section>

<!-- about -->
<section class="about">
  <div class="placeholder" role="img" aria-label="Isometric illustration of a data screen with shields, data nodes and two people working"
       style="left:0;top:724px;width:554px;height:407px;border-radius:50%;background:radial-gradient(ellipse at center,#d3eeee 0%,#e9f3f6 45%,rgba(255,255,255,0) 72%)"></div>
  <div class="abs eyebrow" style="left:591px;top:784px">ABOUT US</div>
  <h2 class="display abs about__title">Advanced data<br>privacy Provider</h2>
  <p class="abs about__text">This is Photoshop's version &nbsp;of Lorem Ipsum. Proin gravida nibh vel velit auctor aliquet aenean sollicitudin, lorem quis bibendum auctor, nisi elit consequat ipsum, nec sagittis sem nibh id elit. Duis sed odio sit amet nibh vulputate cursus a sit amet mauris. Morbi accumsan ipsum velit. Nam nec tellus a odio tincidunt auctor a ornare odio. Sed non &nbsp;mauris vitae erat consequat auctor eu in elit.</p>
  <div class="btn btn--outline" style="left:590px;top:1089px;width:135px;height:39px">Read more</div>
</section>

<!-- services -->
<section class="services">
  <h2 class="abs services__title display">Our Services</h2>
  <p class="abs services__sub">This is Photoshop's version &nbsp;of Lorem Ipsum. Proin gravida nibh .</p>

  <article class="service-card" style="left:89px">
    <svg width="66" height="76" viewBox="0 0 66 76" fill="none" stroke="#0c7a8c" stroke-width="2.2" aria-hidden="true">
      <path d="M31 3 L57 13 V36 C57 54 45 66 31 72 C17 66 5 54 5 36 V13 Z"/>
      <path d="M31 10 L50 17 V36 C50 50 41 59 31 64 C21 59 12 50 12 36 V17 Z"/>
      <ellipse cx="31" cy="27" rx="9" ry="4"/><path d="M22 27 V43 C22 46 40 46 40 43 V27"/><path d="M22 35 C22 38 40 38 40 35"/>
      <circle cx="50" cy="62" r="11" fill="#fff"/><rect x="45" y="61" width="10" height="7"/><path d="M47 61 V58 A3 3 0 0 1 53 58 V61"/>
    </svg>
    <h3>Data privacy (GDPR)</h3>
    <p>This is Photoshop's version &nbsp;of Lorem Ipsum. Proin gravida nibh vel velit .</p>
    <span class="link">Read more</span>
  </article>

  <article class="service-card" style="left:346px">
    <svg width="70" height="72" viewBox="0 0 70 72" fill="none" stroke="#0c7a8c" stroke-width="2.2" aria-hidden="true">
      <rect x="3" y="3" width="64" height="46" rx="2"/><rect x="9" y="9" width="52" height="34"/>
      <path d="M29 49 L26 60 H44 L41 49"/><rect x="4" y="60" width="62" height="9" rx="2"/>
      <rect x="15" y="14" width="8" height="6"/><rect x="44" y="32" width="8" height="6"/><path d="M19 20 V35 H44 M19 27 H33 V32"/><circle cx="36" cy="18" r="3"/>
    </svg>
    <h3>Computer science</h3>
    <p>This is Photoshop's version &nbsp;of Lorem Ipsum. Proin gravida nibh vel velit .</p>
    <span class="link">Read more</span>
  </article>

  <article class="service-card" style="left:606px">
    <svg width="72" height="72" viewBox="0 0 72 72" fill="none" stroke="#0c7a8c" stroke-width="2.2" aria-hidden="true">
      <path d="M26 10 L46 17 V36 C46 52 37 62 26 67 C15 62 6 52 6 36 V17 Z"/>
      <circle cx="26" cy="31" r="6"/><path d="M15 50 C17 42 35 42 37 50"/>
      <rect x="38" y="3" width="30" height="20" rx="2"/><circle cx="53" cy="13" r="5"/>
      <circle cx="48" cy="58" r="10" fill="#fff"/><path d="M43 58 L47 62 L54 54"/>
    </svg>
    <h3>Secure Managed IT</h3>
    <p>This is Photoshop's version &nbsp;of Lorem Ipsum. Proin gravida nibh vel velit .</p>
    <span class="link">Read more</span>
  </article>

  <article class="service-card" style="left:863px">
    <svg width="64" height="76" viewBox="0 0 64 76" fill="none" stroke="#0c7a8c" stroke-width="2.2" aria-hidden="true">
      <rect x="10" y="3" width="46" height="58"/><rect x="4" y="9" width="46" height="58" fill="#fff"/>
      <path d="M11 20 H42 M11 28 H42 M11 36 H42 M11 44 H32 M11 52 H28"/>
      <circle cx="46" cy="60" r="11" fill="#fff"/><path d="M41 60 L45 64 L52 56"/>
    </svg>
    <h3>Compliance</h3>
    <p>This is Photoshop's version &nbsp;of Lorem Ipsum. Proin gravida nibh vel velit .</p>
    <span class="link">Read more</span>
  </article>
</section>

<!-- projects -->
<section class="projects">
  <h2 class="display abs projects__title">Success Project<br>From Previous</h2>
  <p class="abs projects__text">This is Photoshop's version &nbsp;of Lorem Ipsum. Proin gravida nibh vel velit auctor aliquet aenean .</p>
  <div class="btn btn--outline" style="left:86px;top:2315px;width:136px;height:37px">View all</div>

  <div class="project-tile" style="left:570px" role="img" aria-label="Photo of a dark monitor showing lines of code">
    <div class="placeholder" style="inset:0;background:linear-gradient(160deg,#2a3138,#121619)"></div>
    <span>Secure<br>Managed IT</span>
  </div>
  <div class="project-tile" style="left:829px" role="img" aria-label="Illustration of a padlock on a circuit board pattern">
    <div class="placeholder" style="inset:0;background:linear-gradient(160deg,#1b4f6e,#0e2b45)"></div>
    <span>Cyber<br>Security</span>
  </div>
  <div class="project-tile" style="left:1089px;width:111px" role="img" aria-label="Photo of code on a screen">
    <div class="placeholder" style="inset:0;background:linear-gradient(160deg,#2b2452,#14122a)"></div>
    <span style="left:38px;white-space:nowrap">Threat<br>Hunter</span>
  </div>
</section>

<!-- blog -->
<section class="blog">
  <h2 class="display abs blog__title">Latest News From Blog</h2>
  <p class="abs blog__sub">This is Photoshop's version &nbsp;of Lorem Ipsum. Proin gravida nibh .</p>

  <article class="post" style="left:89px">
    <div class="post__image" role="img" aria-label="Photo of a person working on a laptop with code on screen" style="background:linear-gradient(140deg,#3c4650,#1a2026)"></div>
    <h3>Blog heading here</h3>
    <p>Lorem Ipsum is simply dummy text of the printing and typesetting industry. Lorem Ipsum has been the industry's.</p>
    <span class="link">Read more</span>
  </article>
  <article class="post" style="left:433px">
    <div class="post__image" role="img" aria-label="Photo of a hand touching a glowing digital security interface" style="background:linear-gradient(140deg,#0d3c63,#1b6fa8)"></div>
    <h3>Blog heading here</h3>
    <p>Lorem Ipsum is simply dummy text of the printing and typesetting industry. Lorem Ipsum has been the industry's.</p>
    <span class="link">Read more</span>
  </article>
  <article class="post" style="left:779px">
    <div class="post__image" role="img" aria-label="Photo of a finger touching a glowing digital globe" style="background:linear-gradient(140deg,#1a1440,#6b3c8c)"></div>
    <h3>Blog heading here</h3>
    <p>Lorem Ipsum is simply dummy text of the printing and typesetting industry. Lorem Ipsum has been the industry's.</p>
    <span class="link">Read more</span>
  </article>
</section>

<!-- newsletter -->
<section class="newsletter">
  <h2>Newsletter</h2>
  <p>Subscribe to our newsletter</p>
  <div class="newsletter__field">Email Address</div>
  <div class="newsletter__submit">SUBSCRIBE</div>
</section>

<!-- footer -->
<footer>
  <div class="brand" style="left:88px;top:3556px">
    <span class="brand__mark" style="background:var(--green)"></span>
    <span class="brand__name" style="color:#ffffff;font-size:17px">Laurent Dubreuil Conseil</span>
  </div>

  <div class="footer-col" style="left:399px">
    <h4>Services</h4>
    <ul><li>Threat Hunter</li><li>Incident Responder</li><li>Secure Managed IT</li><li>Compliance</li><li>Cyber Security</li><li>Disaster Planning</li></ul>
  </div>
  <div class="footer-col" style="left:610px">
    <h4>Quick Support</h4>
    <ul><li>Contact Us</li><li>FAQ</li><li>Privacy Policy</li><li>Terms &amp; Conditions</li><li>Team</li></ul>
  </div>
  <div class="footer-col" style="left:862px">
    <h4>Contact Info</h4>
    <ul>
      <li class="contact-line"><svg width="10" height="12" viewBox="0 0 10 12"><path d="M5 0 A4.5 4.5 0 0 1 9.5 4.5 C9.5 8 5 12 5 12 C5 12 .5 8 .5 4.5 A4.5 4.5 0 0 1 5 0Z" fill="#24ad8e"/><circle cx="5" cy="4.5" r="1.7" fill="#0a2c4b"/></svg>Some goes address here</li>
      <li class="contact-line"><svg width="11" height="9" viewBox="0 0 11 9"><rect width="11" height="9" rx="1" fill="#24ad8e"/><path d="M0.5 1 L5.5 5 L10.5 1" stroke="#0a2c4b" fill="none"/></svg>contact@ldconseil.fr</li>
      <li class="contact-line"><svg width="11" height="11" viewBox="0 0 11 11"><path d="M2 0 L4 2.5 L3 4 C4 6 5 7 7 8 L8.5 7 L11 9 L9.5 11 C4.5 10.5 .5 6.5 0 1.5Z" fill="#24ad8e"/></svg>+33 1 84 60 27 19</li>
      <li class="contact-line"><svg width="11" height="11" viewBox="0 0 11 11"><circle cx="5.5" cy="5.5" r="5" fill="none" stroke="#24ad8e"/><path d="M.5 5.5 H10.5 M5.5 .5 C3 3 3 8 5.5 10.5 C8 8 8 3 5.5 .5" stroke="#24ad8e" fill="none"/></svg>www.laurentdubreuil-conseil.fr</li>
    </ul>
    <div class="socials" aria-label="Social networks"><i></i><i></i><i></i><i></i></div>
  </div>

  <p class="abs copyright">Copyright @2022. All Rights Reserved.</p>
  <p class="abs legal" style="left:828px">Terms &amp; Conditions</p>
  <p class="abs legal" style="left:1006px">Privacy Policy</p>
  <div class="abs to-top" aria-label="Back to top">
    <svg width="12" height="8" viewBox="0 0 12 8"><path d="M1 7 L6 2 L11 7" stroke="#fff" stroke-width="2" fill="none"/></svg>
  </div>
</footer>

</body>
</html>
```